TarnoJet - where frequent flyers can cash out their airline miles

TarnoJet enable the trade of airline miles between individuals. Our landing page which I want to redesign should refer to individuals who have miles in airline loyalty programs and would like to sell them with our platform

I would like to get a landing page design with a look and feel much more advanced and appealing then the one we currently have.

Page should include the information and fields in our current landing page but should be more professional and include except for the current two partner's logos and our logo of course, also the attached banner of stayvenko.example with a link to stayvenko.example with our affiliate code.

Audience of our web page is business men and heavy travellers therefore, page should reflect professionalism and should be business wise. There could be something that has to do with airplanes and money in terms of the background and pictures shows.

Additional text (on top of the short description at tarnojet.example is -
"
TarnoJet™ converts frequent flyers' accumulated miles to exceptionally low-priced flight tickets. It serves as an online trading platform for sellers of miles and buyers of flight tickets, offering airline customers a fully automated process whereby flight tickets are created out of loyalty club miles.
"

Our web site as a reference is www.tarnojet.example

Target Market(s)

Business men who are heavily travellers

Industry/Entity Type

Travel Industry

Number of Pages Required

1 page

Font styles to use
Sans Serif

Colors
85acd3
0255a3

Requirements
Must have
• Our logo and the 3 logos mentioned at the description. It should have on the top the look & Feel that it currently has on our landing page - www.tarnojet.example
Nice to have
• I would like people entering the web page to love it and for them to leave the relevant details so we get back to them
Should not have
• Not too many texts or images. Don't want people to scroll down too much if at all

```html
<!DOCTYPE html>
<html lang="en">
<head>
<meta charset="utf-8">
<title>TarnoJet – Sell Your Miles</title>
<link rel="stylesheet" href="https://fonts.googleapis.com/css2?family=Roboto:wght@400;500;700&display=swap">
<style>
:root{
  --brand:#0255a3;
  --brand-light:#85acd3;
  --ink:#222;
  --text:#666;
  --label:#555;
  --line:#d6d6d6;
  --green:#86bf3a;
  --green-dark:#74a92f;
  --white:#fff;
}
*{box-sizing:border-box;margin:0;padding:0}
html,body{width:1200px;height:1173px;overflow:hidden;background:var(--white)}
body{font-family:'Roboto',sans-serif;color:var(--text);position:relative}

.top-rule{position:absolute;left:0;top:0;width:1200px;height:3px;background:var(--brand)}

.site-header{position:absolute;left:0;top:3px;width:1200px;height:100px;background:var(--white)}
.brand{position:absolute;left:84px;top:16px}
.brand-name{display:flex;align-items:center;gap:8px;font-size:40px;font-weight:700;color:var(--ink);letter-spacing:-1px;line-height:1}
.brand-name .mark{width:14px;height:14px;background:var(--ink)}
.brand-tag{display:block;text-align:right;font-size:13px;font-weight:500;color:var(--ink);margin-top:14px}

.call-tab{position:absolute;left:867px;top:0;width:246px;height:42px}
.call-tab .tab-shape{position:absolute;left:0;top:0}
.call-label{position:absolute;left:30px;top:0;height:42px;color:var(--white);font-size:13px;display:flex;align-items:center;gap:10px;white-space:nowrap}
.call-label svg{flex:0 0 auto}

.main-nav{position:absolute;top:68px;left:573px;font-size:13px;font-weight:500}
.main-nav a{color:#555;text-decoration:none;position:absolute;white-space:nowrap}
.main-nav a.active{color:var(--brand)}

.hero{position:absolute;left:0;top:103px;width:1200px;height:596px;
  background:linear-gradient(180deg,#8fc1db 0%,#b9d8e6 40%,#7fb6c9 62%,#d9dcd8 78%,#cfcac0 100%)}
.hero-dots{position:absolute;left:86px;top:562px;display:flex;gap:6px}
.hero-dots i{width:12px;height:12px;border:1.5px solid var(--white);border-radius:50%;display:block}
.hero-dots i.on{border-color:var(--brand)}

.sell-tab{position:absolute;left:473px;top:202px;width:182px;height:51px}
.sell-tab svg{position:absolute;left:0;top:0}
.sell-tab h2{position:absolute;left:20px;top:16px;color:var(--white);font-size:17px;font-weight:500}

.sell-panel{position:absolute;left:473px;top:253px;width:641px;height:350px;background:var(--white)}
.sell-panel h3{position:absolute;left:18px;font-size:15px;font-weight:500;color:var(--label)}
.field{position:absolute;height:33px;border:1px solid var(--line);font-size:13px;color:#777;padding:9px 10px 0}
.btn-search{position:absolute;left:19px;top:286px;width:126px;height:40px;background:var(--green);
  border-bottom:2px solid var(--green-dark);color:var(--white);font-size:15px;font-weight:500;
  display:flex;align-items:center;justify-content:center;gap:14px}

.welcome{position:absolute;left:85px;top:732px;width:625px}
.welcome h1{font-size:19px;font-weight:700;color:#555;margin-bottom:12px}
.welcome h1 em{font-style:normal;color:var(--brand)}
.welcome p{font-size:13px;line-height:25px;margin-bottom:18px}

.partner{position:absolute;top:987px;width:149px;height:66px;border:1px solid #e2e2e2;
  display:flex;align-items:center;justify-content:center;gap:6px;font-size:14px;font-weight:700}
.partner .badge{width:34px;height:34px;border-radius:50%}

.promo{position:absolute;left:784px;top:744px;width:321px;height:307px;border:1px solid #e2e2e2;padding:4px}
.promo a{display:block;position:relative;width:311px;height:297px;text-decoration:none;
  background:linear-gradient(180deg,#0f4aa0 0%,#0f4aa0 27%,#3a9ad0 33%,#7ec6e3 50%,#e6dcc8 72%,#bfdbe6 100%)}
.promo .title{position:absolute;top:6px;width:100%;text-align:center;color:var(--white);font-size:25px;font-weight:500}
.promo .sub{position:absolute;top:40px;width:100%;text-align:center;color:var(--white);font-size:16px}
.promo .cta{position:absolute;left:102px;top:215px;width:108px;height:38px;background:#1976e6;border:2px solid var(--white);
  color:var(--white);font-size:18px;text-align:center;line-height:34px}
.promo .site{position:absolute;top:262px;width:100%;text-align:center;color:var(--white);font-size:20px;font-weight:700}

.site-footer{position:absolute;left:0;top:1093px;width:1200px;height:80px;background:var(--brand)}
.site-footer small{position:absolute;left:89px;top:33px;color:var(--white);font-size:11px}
.social{position:absolute;left:890px;top:24px;display:flex;gap:10px}
.social a{width:36px;height:36px;border:2px solid var(--white);border-radius:50%;display:block}
</style>
</head>
<body>
<div class="top-rule"></div>

<header class="site-header">
  <div class="brand">
    <div class="brand-name"><span class="mark"></span>TARNOJET</div>
    <span class="brand-tag">Loyalty Pays</span>
  </div>

  <div class="call-tab">
    <svg class="tab-shape" width="246" height="42"><polygon points="0,0 246,0 232,42 12,42" fill="#0255a3"/></svg>
    <span class="call-label">
      <svg width="16" height="12" viewBox="0 0 16 12"><path d="M1 4 Q8 -1 15 4 L13 6 L11 4 L5 4 L3 6 Z" fill="#fff"/><rect x="3" y="6" width="10" height="6" rx="1" fill="#fff"/></svg>
      CALL US : (0000-482-7730
    </span>
  </div>

  <nav class="main-nav">
    <a class="active" style="left:0">HOME</a>
    <a style="left:78px">HOTEL</a>
    <a style="left:160px">FLIGHTS</a>
    <a style="left:253px">TOURS</a>
    <a style="left:336px">TRAVEL GUIDE</a>
    <a style="left:463px">CONTACT US</a>
  </nav>
</header>

<section class="hero" role="img" aria-label="Photo of travellers relaxing in deck chairs on a tropical beach with palm trees and a plane in the sky">
  <div class="hero-dots"><i></i><i></i><i class="on"></i><i></i><i></i></div>
</section>

<div class="sell-tab">
  <svg width="182" height="51"><polygon points="0,0 162,0 182,51 0,51" fill="#0255a3"/></svg>
  <h2>SELL YOUR MILES</h2>
</div>

<form class="sell-panel">
  <h3 style="top:28px">PERSONAL DETAILS :</h3>
  <div class="field" style="left:20px;top:58px;width:193px">First Name :</div>
  <div class="field" style="left:223px;top:58px;width:193px">Phone Number :</div>
  <div class="field" style="left:428px;top:58px;width:193px">Email :</div>

  <h3 style="top:114px">AIRLINES DETAILS :</h3>
  <div class="field" style="left:20px;top:144px;width:290px">Airline #1 :</div>
  <div class="field" style="left:330px;top:144px;width:290px">Amount of Miles :</div>
  <div class="field" style="left:20px;top:186px;width:290px">Airline #2 :</div>
  <div class="field" style="left:330px;top:186px;width:290px">Amount of Miles :</div>
  <div class="field" style="left:20px;top:228px;width:290px">Airline #3 :</div>
  <div class="field" style="left:330px;top:228px;width:290px">Amount of Miles :</div>

  <div class="btn-search">
    <svg width="16" height="16" viewBox="0 0 16 16"><circle cx="6.5" cy="6.5" r="4.7" fill="none" stroke="#fff" stroke-width="2.2"/><line x1="10" y1="10" x2="14.5" y2="14.5" stroke="#fff" stroke-width="2.6" stroke-linecap="round"/></svg>
    SEARCH
  </div>
</form>

<section class="welcome">
  <h1>WELCOME TO <em>TARNOJET</em></h1>
  <p>It is a long established fact that a reader will be distracted by the readable content of a page when looking at its lay out. The point of using Lorem Ipsum is that it has a more-or-less normal distribution of letters, as opposed to using Content here, content here', making it look like readable English.Many desktop publishing packages and web page editors now use Lorem Ipsum as their default model text, and a search for 'lorem ipsum' will uncover many web site till in their infancy.....</p>
  <p>Making it look like readable English.Many desktop publishing packages and web page editors now use and a search for 'lorem ipsum' will uncover many web site till in their infancy.....</p>
</section>

<div class="partner" style="left:84px;color:#d0202a"><span class="badge" style="background:#d0202a"></span>Varello Tours</div>
<div class="partner" style="left:256px;color:#3d4d5c"><span class="badge" style="background:#3d4d5c;border-radius:4px"></span>Quindle Zone</div>

<aside class="promo">
  <a href="https://stayvenko.example" role="img" aria-label="Banner photo of a beach with thatched umbrellas and a pool">
    <span class="title">Vacation of a Lifetime</span>
    <span class="sub">Book a slice of paradise</span>
    <span class="cta">Book now</span>
    <span class="site">stayvenko.example</span>
  </a>
</aside>

<footer class="site-footer">
  <small>© Copy Rights 2015 .TarnoJet.All Rights Reserved.</small>
  <div class="social" aria-label="Social links"><a></a><a></a><a></a><a></a><a></a></div>
</footer>
</body>
</html>
```